Business card/stationary for non profit organization
Business card and Stationary for non profit organization
Business card/stationary for non profit organization - Children
Creative Brief
Bright & Fun-filled
Mr. Fenwick
Founder
517 Bellmore Lane Suite 309 Linden Hollow, New York 10599
fenwick@mrfenwickcommons.org
www.mrfenwickcommons.org
Please have the logo on the back of the business card and room for a tagline.
Concepts
Business Cards for kids golf

```html
<!DOCTYPE html>
<html lang="en">
<head>
<meta charset="utf-8">
<title>Mr. Fenwick Commons — Business Card</title>
<link rel="stylesheet" href="https://fonts.googleapis.com/css2?family=Open+Sans:wght@300;400;700&display=swap">
<style>
  :root {
    --backdrop: #d9d9d9;
    --card: #ffffff;
    --ink: #1b1b1b;
    --gold: #b8952f;
    --text: #5a5a5a;
    --text-soft: #7a7a7a;
  }
  * { margin: 0; padding: 0; box-sizing: border-box; }
  html, body {
    width: 1200px; height: 984px; overflow: hidden;
    background: var(--backdrop);
    font-family: "Open Sans", Arial, sans-serif;
  }
  .sheet {
    width: 1200px; height: 984px;
    display: flex; flex-direction: column;
    align-items: center; justify-content: center; gap: 40px;
  }
  .card {
    position: relative;
    width: 770px; height: 440px;
    background: var(--card);
    border-radius: 26px;
    overflow: hidden;
  }
  .brand { display: flex; align-items: center; gap: 16px; }
  .brand-dot {
    width: 34px; height: 34px; border-radius: 50%;
    background: var(--gold); flex: none;
  }
  .brand-name {
    font-weight: 700; font-size: 26px; color: var(--ink);
    letter-spacing: 0.04em; text-transform: uppercase; white-space: nowrap;
  }
  .card-front { display: flex; align-items: center; justify-content: center; }
  .card-back .stripes {
    position: absolute; left: 66px; top: 0;
    width: 40px; height: 150px;
  }
  .card-back .details {
    position: absolute; left: 150px; top: 52px;
    color: var(--text);
  }
  .person-name { font-weight: 400; font-size: 36px; color: var(--text); line-height: 1.15; }
  .person-role { font-weight: 400; font-size: 22px; color: var(--text); margin-bottom: 20px; }
  .address { font-weight: 300; font-size: 18px; line-height: 1.45; color: var(--text-soft); white-space: nowrap; }
  .contact {
    position: absolute; left: 90px; top: 250px;
    list-style: none;
  }
  .contact li {
    display: flex; align-items: center; gap: 30px;
    font-weight: 300; font-size: 18px; line-height: 30px; color: var(--text-soft);
    white-space: nowrap;
  }
  .contact .bullet {
    width: 12px; height: 12px; border-radius: 50%;
    background: var(--ink); border: 2px solid var(--gold); flex: none;
  }
  .card-back .brand { position: absolute; right: 40px; top: 204px; }
  .card-back .brand-dot { width: 28px; height: 28px; }
  .card-back .brand-name { font-size: 22px; }
</style>
</head>
<body>
<main class="sheet">
  <section class="card card-front" aria-label="Card front">
    <div class="brand">
      <span class="brand-dot"></span>
      <span class="brand-name">Mr. Fenwick Commons</span>
    </div>
  </section>

  <section class="card card-back" aria-label="Card back">
    <svg class="stripes" viewBox="0 0 40 150" aria-hidden="true">
      <rect x="0" y="0" width="10" height="150" fill="#1b1b1b"/>
      <rect x="14" y="0" width="12" height="150" fill="#b8952f"/>
      <rect x="30" y="0" width="10" height="150" fill="#1b1b1b"/>
    </svg>
    <div class="details">
      <p class="person-name">Mr. Fenwick</p>
      <p class="person-role">Founder</p>
      <p class="address">517 Bellmore Lane Suite 309<br>Linden Hollow, New York 10599</p>
    </div>
    <ul class="contact">
      <li><span class="bullet"></span>914-555-0172</li>
      <li><span class="bullet"></span>914-555-0172</li>
      <li><span class="bullet"></span>fenwick@mrfenwickcommons.org</li>
      <li><span class="bullet"></span>www.mrfenwickcommons.org</li>
    </ul>
    <div class="brand">
      <span class="brand-dot"></span>
      <span class="brand-name">Mr. Fenwick Commons</span>
    </div>
  </section>
</main>
</body>
</html>
```